Electrical Business Card Design

New electrical business targeting my local area
Installations
Repairs
Switchboards
TV / Vistacast / Antennas
Telephone
Data Networks
Audio Visual
Licence # 518247K
ABN 63918257041
I would like some white background, black writing, red, blue & green can be used
Designer discretion to be used on layout, colour placement & any images
Updates
Project Deadline Extended
Reason: To give designers more time, I thought 5 days wasn't enough
Please don't just create generic business cards................include personal details e.g. business name, contact name, ph #, email. Also include the things I do, licence # & abn (refer to brief for all details)
Thanks
Project Deadline Extended
Reason: Would like more designs & have now committed my payment, thank you
Industry/Entity Type
Electrical
Contact Information for Business Card
Korvale Electrical Services,
Derek Halloran,
0498 351 672,
korvaleelectrical@plumnet.net.au,
My suburb is Ryde
Look and feel

```html
<!DOCTYPE html>
<html lang="en">
<head>
<meta charset="utf-8">
<title>Korvale Electrical Services – Business Card</title>
<link href="https://fonts.googleapis.com/css2?family=Aldrich&display=swap" rel="stylesheet">
<style>
  :root {
    --page: #e9e7e3;
    --card-blue: #3c3f98;
    --accent-blue: #14a3dd;
    --stripe-dark: #1e1e24;
    --paper: #ffffff;
    --paper-shade: #d9d9dc;
    --ink-light: #ffffff;
    --brand-ink: #3c3f98;
  }
  html, body {
    margin: 0;
    padding: 0;
    width: 1115px;
    height: 1200px;
    overflow: hidden;
    background: var(--page);
    font-family: "Aldrich", "Segoe UI", sans-serif;
  }
  .card {
    position: absolute;
    left: 107px;
    top: 340px;
    width: 900px;
    height: 520px;
    box-shadow: 0 18px 40px rgba(0,0,0,0.25);
  }
  .card-art {
    position: absolute;
    inset: 0;
    display: block;
  }
  .brand-block {
    position: absolute;
    left: 34px;
    top: 178px;
    width: 350px;
    color: var(--brand-ink);
  }
  .brand-name {
    margin: 0;
    font-size: 32px;
    font-weight: 400;
    line-height: 1.2;
  }
  .service-list {
    list-style: none;
    margin: 22px 0 0;
    padding: 0;
    font-size: 15px;
    line-height: 1.6;
  }
  .contact-block {
    position: absolute;
    right: 42px;
    top: 78px;
    text-align: right;
    color: var(--ink-light);
  }
  .person-name {
    margin: 0;
    font-size: 30px;
    font-weight: 400;
    letter-spacing: 1px;
  }
  .person-role {
    margin: 4px 0 0;
    font-size: 21px;
  }
  .credentials {
    margin: 56px 0 0;
    font-size: 21px;
    line-height: 1.5;
  }
  .contact-list {
    list-style: none;
    margin: 30px 0 0;
    padding: 0;
    font-size: 18px;
  }
  .contact-list li {
    display: flex;
    justify-content: flex-end;
    align-items: center;
    gap: 12px;
    height: 38px;
  }
  .contact-list svg {
    width: 20px;
    height: 20px;
    flex: none;
    fill: none;
    stroke: var(--ink-light);
    stroke-width: 2;
  }
</style>
</head>
<body>
  <section class="card">
    <svg class="card-art" viewBox="0 0 900 520" aria-hidden="true">
      <defs>
        <linearGradient id="paperGradient" x1="0" y1="0" x2="1" y2="1">
          <stop offset="0" stop-color="var(--paper-shade)"/>
          <stop offset="0.45" stop-color="var(--paper)"/>
          <stop offset="1" stop-color="var(--paper-shade)"/>
        </linearGradient>
      </defs>
      <rect class="card-field" width="900" height="520" fill="var(--card-blue)"/>
      <path class="stripe-dark" d="M0,0 H395 C425,150 465,260 425,360 C385,440 325,500 255,520 H0 Z" fill="var(--stripe-dark)"/>
      <path class="stripe-accent" d="M0,0 H384 C414,150 454,260 414,360 C374,440 314,500 244,520 H0 Z" fill="var(--accent-blue)"/>
      <path class="paper-panel" d="M0,0 H365 C395,150 432,260 394,360 C354,440 294,500 224,520 H0 Z" fill="url(#paperGradient)"/>
    </svg>

    <div class="brand-block">
      <h1 class="brand-name">Korvale Electrical<br>Services</h1>
      <ul class="service-list">
        <li>Installations · Repairs · Switchboards</li>
        <li>TV / Vistacast / Antennas · Telephone</li>
        <li>Data Networks · Audio Visual</li>
      </ul>
    </div>

    <div class="contact-block">
      <h2 class="person-name">DEREK HALLORAN</h2>
      <p class="person-role">Managing Director</p>
      <p class="credentials">Licence # 518247K<br>ABN 63918257041</p>
      <ul class="contact-list">
        <li>0498 351 672
          <svg viewBox="0 0 24 24"><path d="M5 3h4l2 5-3 2a12 12 0 0 0 6 6l2-3 5 2v4a2 2 0 0 1-2 2A18 18 0 0 1 3 5a2 2 0 0 1 2-2z"/></svg>
        </li>
        <li>0498 351 672
          <svg viewBox="0 0 24 24"><rect x="6" y="2" width="12" height="20" rx="2"/><line x1="11" y1="18" x2="13" y2="18"/></svg>
        </li>
        <li>Ryde, NSW
          <svg viewBox="0 0 24 24"><path d="M12 22s7-7 7-12a7 7 0 0 0-14 0c0 5 7 12 7 12z"/><circle cx="12" cy="10" r="2.5"/></svg>
        </li>
        <li>korvaleelectrical@plumnet.net.au
          <svg viewBox="0 0 24 24"><rect x="3" y="5" width="18" height="14"/><path d="M3 5l9 8 9-8"/></svg>
        </li>
      </ul>
    </div>
  </section>
</body>
</html>
```